Fun, Clean Business Card For Family Focused Travel Agency

I need a business card using specific colors and fonts as in the uploaded files. Ideally, I would like a large image of the logo on the back and all the contact info on the front. Maybe the stars/dots somewhere in a flowy form.

I do want it the contact information to be clear and easy to read. I don't want it to look too busy. Maybe even a bit minimalist.

I plan or ordering the ROUNDED CORNER business cards from Cardwell Press, so please consider that in your design.

Target Market(s)

Families with children, couples, groups of friends

Contact Information for Business Card

Marla Quent, Owner
Marla@TidewayTrips.example
Cell Phone Number 555-218-6034
Office Phone Number 555-647-1295
Specializing in Fablecrest destinations, Goldmere Parkside Resort, Cruises and All-Inclusive Vacations.

Nice but not required:
www.TidewayTrips.example
Facebook, Instagram, Twitter icons with username: TidewayTrips

Font styles to use
Sans Serif

Requirements
Must have
• Please try to use the colors from the logo as much as possible. I understand lighter shades/colors may be needed for some things.
Should not have
• NO SERIF FONTS. That is really the only thing I do not want at all

```html
<!DOCTYPE html>
<html lang="en">
<head>
<meta charset="utf-8">
<title>Tideway Trips – Business Card</title>
<link href="https://fonts.googleapis.com/css2?family=Fira+Sans:wght@300;400;500;700&display=swap" rel="stylesheet">
<style>
  :root{
    --navy:#0c1128;
    --teal:#05b08f;
    --orange:#f07a1c;
    --blue:#1a9fd8;
    --gold:#dcad27;
    --green:#8dc040;
    --grey-text:#5d5d5d;
    --stage:#cbcac8;
    --paper:#ffffff;
    --mist:#bfe9df;
  }
  *{margin:0;padding:0;box-sizing:border-box}
  html,body{width:1200px;height:1200px;overflow:hidden}
  body{background:var(--stage);position:relative;font-family:"Fira Sans",sans-serif;color:var(--grey-text)}
  .card{position:absolute;left:180px;width:840px;height:480px;background:var(--paper);overflow:hidden}
  .card--front{top:94px}
  .card--back{top:616px}

  .stripe-top{position:absolute;top:0;left:0;width:100%;height:10px;display:flex}
  .stripe-top span{flex:1}
  .stripe-side{position:absolute;top:0;right:0;width:9px;height:100%;display:flex;flex-direction:column}
  .stripe-side span{flex:1}
  .c-orange{background:var(--orange)} .c-blue{background:var(--blue)} .c-navy{background:var(--navy)}
  .c-teal{background:var(--teal)} .c-gold{background:var(--gold)} .c-green{background:var(--green)}

  .wave-field{position:absolute;left:0;right:0;bottom:0;height:260px;
    background:radial-gradient(ellipse at 60% 80%,rgba(191,233,223,.55),rgba(191,233,223,0) 70%)}

  .brand{position:absolute;left:124px;top:150px;display:flex;align-items:center;gap:30px}
  .brand__dot{width:150px;height:150px;border-radius:50%;background:var(--teal)}
  .brand__name{font-weight:700;font-size:86px;line-height:1;color:var(--navy);letter-spacing:-1px}
  .website{position:absolute;left:0;right:0;top:532px;top:432px;text-align:center;font-size:18px;letter-spacing:5px;color:var(--navy)}

  .side-panel{position:absolute;left:0;top:0;width:151px;height:100%;background:var(--teal)}
  .side-panel__haze{position:absolute;inset:0;background:radial-gradient(ellipse at 70% 55%,rgba(255,255,255,.18),rgba(255,255,255,0) 65%)}
  .icon{position:absolute;left:104px;width:26px;height:26px;fill:#0e8a70}

  .social{position:absolute;top:18px;right:37px;font-size:19px;color:var(--grey-text)}
  .contact{position:absolute;left:173px;top:0}
  .name{position:absolute;top:130px;white-space:nowrap;font-size:37px;font-weight:300;color:var(--grey-text)}
  .name strong{font-weight:500;color:var(--orange)}
  .role{position:absolute;top:176px;font-size:17px}
  .line{position:absolute;white-space:nowrap;font-size:24px;font-weight:300}
  .specialty{position:absolute;top:210px;top:345px;width:420px;font-size:24px;font-weight:300;line-height:32px}
  .specialty .hl-orange{color:var(--orange);font-weight:400}
  .specialty .hl-navy{color:var(--navy);font-weight:400}
  .specialty .hl-teal{color:var(--teal);font-weight:400}
  .specialty .hl-blue{color:var(--blue);font-weight:400}
  .back-brand{position:absolute;left:580px;top:180px;width:220px;text-align:center}
  .back-brand__dot{width:120px;height:120px;border-radius:50%;background:var(--teal);margin:0 auto 14px}
  .back-brand__name{font-weight:700;font-size:32px;color:var(--navy)}
</style>
</head>
<body>
  <section class="card card--front">
    <div class="stripe-top">
      <span class="c-orange"></span><span class="c-blue"></span><span class="c-navy"></span><span class="c-teal"></span><span class="c-gold"></span>
      <span class="c-green"></span><span class="c-orange"></span><span class="c-blue"></span><span class="c-navy"></span><span class="c-teal"></span>
    </div>
    <div class="wave-field" role="img" aria-label="Flowing wave of small mint dots"></div>
    <div class="brand">
      <div class="brand__dot"></div>
      <div class="brand__name">Tideway Trips</div>
    </div>
    <p class="website">www.TidewayTrips.example</p>
  </section>

  <section class="card card--back">
    <div class="side-panel">
      <div class="side-panel__haze" role="img" aria-label="Faint swirl of white dots on teal"></div>
      <svg class="icon" style="top:138px" viewBox="0 0 24 24"><circle cx="12" cy="7" r="5"/><path d="M3 23c0-6 4-9 9-9s9 3 9 9z"/></svg>
      <svg class="icon" style="top:208px" viewBox="0 0 24 24"><path d="M2 5h20v14H2z M3 6l9 7 9-7" stroke="#0a6f5a" stroke-width="1.2"/></svg>
      <svg class="icon" style="top:250px" viewBox="0 0 24 24"><rect x="6" y="1" width="12" height="22" rx="2" fill="none" stroke="#0e8a70" stroke-width="2"/><rect x="10" y="19" width="4" height="1.5"/></svg>
      <svg class="icon" style="top:292px" viewBox="0 0 24 24"><path d="M6 2l4 5-2 3c1 3 3 5 6 6l3-2 5 4-3 4C10 22 2 14 2 5z"/></svg>
      <svg class="icon" style="top:332px" viewBox="0 0 24 24"><rect x="1" y="7" width="22" height="15" rx="2"/><path d="M8 7V4h8v3" fill="none" stroke="#0e8a70" stroke-width="2"/></svg>
    </div>
    <p class="social">@ TidewayTrips</p>
    <div class="contact">
      <h1 class="name"><strong>Marla</strong> Quent</h1>
      <p class="role">Owner</p>
      <p class="line" style="top:206px">Marla@TidewayTrips.example</p>
      <p class="line" style="top:248px">555-218-6034</p>
      <p class="line" style="top:288px">555-647-1295</p>
      <p class="specialty">Specializing in <span class="hl-orange">Fablecrest destinations,</span> <span class="hl-navy">Goldmere Parkside Resort,</span> <span class="hl-teal">Cruises</span> and <span class="hl-blue">All-Inclusive Vacations.</span></p>
    </div>
    <div class="back-brand">
      <div class="back-brand__dot"></div>
      <div class="back-brand__name">Tideway Trips</div>
    </div>
    <div class="stripe-side">
      <span class="c-orange"></span><span class="c-blue"></span><span class="c-navy"></span><span class="c-teal"></span><span class="c-gold"></span>
      <span class="c-green"></span><span class="c-orange"></span><span class="c-blue"></span><span class="c-navy"></span><span class="c-teal"></span>
    </div>
  </section>
</body>
</html>
```